Web Site Design

We need to design the whole web site for our small start up. We sell hospitality and culinary art internships abroad. I did my own design with WIX which is horrible meanwhile I started with my business. You can see it www.brightvoyage-intern.example I will need you to create a new and attractive web site and to leave it working on wix. The internship destinations are United Arab Emirates, Thailand, China, Spain, Brazil and maybe leave a couple of pages for future destinations.You could also get other ideas of other sites that do internships.

Target Market(s)

Students and recent graduates of hospitality and culinary art majors

Industry/Entity Type

Education

Number of Pages Required

5+ page

Requirements
Must have
• Addittional to our program destinations, or to the pages in the current site. The website must contain a page for Universities or Hotels who require our service

```html
<!DOCTYPE html>
<html lang="en">
<head>
<meta charset="utf-8">
<title>Bright Voyage — Hospitality and culinary art internships abroad</title>
<link rel="stylesheet" href="https://fonts.googleapis.com/css2?family=Raleway:wght@400;500;600;700&family=Libre+Baskerville:wght@400;700&display=swap">
<style>
:root{
  --teal:#2a7d7c;
  --teal-light:#35b6c2;
  --heart:#2aa7a3;
  --ink:#1d1d1d;
  --muted:#666;
  --line:#dcdcdc;
  --dark-band:#2e3338;
  --footer:#5b5757;
  --white:#fff;
  --star:#f2a531;
}
*{box-sizing:border-box;margin:0;padding:0}
html,body{width:1200px;height:4306px;overflow:hidden}
body{font-family:"Raleway",Arial,sans-serif;color:var(--ink);background:var(--white);position:relative}
.section{position:absolute;left:0;width:1200px}
.btn{display:inline-block;background:var(--teal);color:var(--white);font-family:"Raleway",sans-serif;font-size:15px;letter-spacing:1px;text-transform:uppercase;border-radius:4px;text-align:center}

/* hero */
.hero{top:0;height:568px;background:linear-gradient(180deg,#3a3a36 0%,#6b5a44 45%,#3d3a36 100%)}
.hero-photo{position:absolute;inset:0;background:radial-gradient(ellipse at 50% 60%,rgba(200,170,120,.45),rgba(30,30,30,.6) 75%)}
.nav{position:absolute;top:28px;left:118px;right:118px;height:50px;display:flex;align-items:center}
.brand{display:flex;align-items:center;gap:14px;color:var(--white);font-family:"Libre Baskerville",serif;font-size:22px;letter-spacing:1px}
.brand-mark{width:46px;height:46px;border:2px solid var(--white);border-radius:50%}
.nav-links{margin-left:auto;display:flex;gap:30px;align-items:center;color:var(--white);font-size:15px}
.nav-cta{padding:11px 22px;border-radius:18px;background:var(--teal);font-size:13px}
.hero-title{position:absolute;top:182px;width:100%;text-align:center;color:var(--white);font-size:46px;font-weight:700;line-height:1.25}
.hero-title .accent{color:#5cc6c4}
.hero-sub{position:absolute;top:290px;width:100%;text-align:center;color:var(--white);font-size:20px;line-height:1.3}
.hero .btn{position:absolute;top:352px;left:528px;width:200px;padding:13px 0}

/* about */
.about{top:568px;height:480px;text-align:center}
.section-title{font-size:32px;font-weight:500;color:var(--ink)}
.about .section-title{margin-top:78px}
.about-intro{margin:30px auto 0;width:560px;font-size:15px;line-height:1.65;color:#444}
.features{display:flex;justify-content:center;gap:42px;margin-top:46px}
.feature{width:210px}
.feature-icon{width:114px;height:114px;margin:0 auto;border:2px solid var(--teal);border-radius:50%;display:flex;align-items:center;justify-content:center}
.feature h3{margin-top:28px;font-size:17px;font-weight:500}
.feature p{margin-top:14px;font-size:11px;line-height:1.6;color:var(--muted)}

/* programs */
.programs{top:1048px;height:1087px}
.programs .section-title{position:absolute;top:45px;width:100%;text-align:center}
.card{position:absolute;width:466px;height:420px;border:1px solid var(--line);background:var(--white)}
.card-photo{height:224px}
.card-meta{display:flex;align-items:center;gap:10px;margin:18px 22px 0;font-size:11px;color:#888}
.stars{color:var(--star);font-size:18px;letter-spacing:1px}
.heart{margin-left:auto}
.card h3{margin:20px 22px 0;font-family:"Libre Baskerville",serif;font-size:18px;font-weight:400;line-height:1.5}
.card-tags{margin:6px 22px 0;font-size:13px;color:#444}
.card .btn{position:absolute;left:22px;bottom:18px;padding:5px 14px;font-size:13px;text-transform:none;letter-spacing:0;border-radius:2px}

/* destinations */
.destinations{top:2135px;height:715px;background:linear-gradient(180deg,#2a2f34,#3a4046 55%,#2b3035)}
.destinations .section-title{position:absolute;top:85px;width:100%;text-align:center;color:var(--white)}
.dest-tile{position:absolute;top:189px;height:318px;border:8px solid #e9dcd6;display:flex;align-items:center;justify-content:center;color:var(--white);font-size:28px;font-weight:600;letter-spacing:1px}
.destinations .btn{position:absolute;top:580px;left:452px;width:320px;padding:14px 0;font-size:14px}

/* articles */
.articles{top:2850px;height:537px}
.articles .section-title{position:absolute;top:68px;width:100%;text-align:center}
.article{position:absolute;top:138px;width:315px}
.article-photo{height:226px}
.article h3{margin-top:26px;font-size:22px;font-weight:600}
.article time{display:block;margin-top:10px;font-size:13px;color:var(--teal)}
.article p{margin-top:6px;font-size:13px;color:#555}

/* contact */
.contact{top:3387px;height:508px;background:var(--teal-light);color:var(--white)}
.contact h2{position:absolute;top:92px;width:100%;text-align:center;font-family:"Libre Baskerville",serif;font-weight:400;font-size:25px;line-height:1.6}
.field{position:absolute;height:34px;border-bottom:1px solid rgba(255,255,255,.85);font-family:"Libre Baskerville",serif;font-size:14px;padding-top:4px}
.send{position:absolute;top:398px;left:448px;width:232px;height:42px;background:#0b0b0b;color:var(--white);font-size:15px;letter-spacing:1px;text-align:center;line-height:42px;border-radius:4px}

/* footer */
.footer{top:3895px;height:411px;background:var(--footer);color:var(--white)}
.footer-col{position:absolute;top:62px}
.footer-col h4{font-size:15px;font-weight:700;letter-spacing:1px;margin-bottom:16px;text-transform:uppercase}
.footer-col li{list-style:none;font-size:12px;line-height:2.1}
.socials{display:flex;gap:10px}
.socials span{width:28px;height:28px;border:1.5px solid var(--white);border-radius:50%}
.newsletter-input{width:266px;height:40px;background:var(--white);color:#555;font-size:12px;padding:12px;border-radius:3px}
.newsletter-btn{margin-top:10px;width:96px;height:32px;background:var(--teal);font-size:13px;text-align:center;line-height:32px;border-radius:3px}
.footer-rule{position:absolute;top:310px;left:170px;right:170px;border-top:1px solid rgba(255,255,255,.2)}
.copyright{position:absolute;top:336px;width:100%;text-align:center;font-size:12px}
</style>
</head>
<body>

<header class="section hero">
  <div class="hero-photo" role="img" aria-label="Chefs working in a busy hotel restaurant kitchen"></div>
  <nav class="nav">
    <div class="brand"><span class="brand-mark"></span>BRIGHT VOYAGE</div>
    <div class="nav-links"><span>Welcome</span><span>Destinations</span><span>Contact</span><span class="nav-cta">GET STARTED</span></div>
  </nav>
  <h1 class="hero-title">Hospitality <span class="accent">and</span> culinary art<br>internships abroad</h1>
  <p class="hero-sub">Take your paid internship in one of our top international<br>five-star hotels</p>
  <span class="btn">Browse Programs</span>
</header>

<section class="section about">
  <h2 class="section-title">About Hospitality /culinary art internships&nbsp; abroad</h2>
  <p class="about-intro">Hospitality internships are our specialty! Take your paid internship in one of our top international five-star hotels</p>
  <div class="features">
    <div class="feature">
      <div class="feature-icon"><svg width="52" height="52" viewBox="0 0 52 52"><circle cx="26" cy="26" r="22" fill="#2a7d7c"/><path d="M14 18c5-2 8 2 12 0s4 6 0 8-6 8-10 4 2-6-2-12z" fill="#fff"/></svg></div>
      <h3>Top 10 Worldwide</h3>
      <p>The Professional Programs here assure a career start in the Hospitality &amp; International Cruise Line Industry.</p>
    </div>
    <div class="feature">
      <div class="feature-icon"><svg width="52" height="52" viewBox="0 0 52 52" fill="none" stroke="#2a7d7c" stroke-width="3"><rect x="10" y="8" width="32" height="38" rx="3"/><path d="M18 26l6 6 10-12"/></svg></div>
      <h3>100% Work Placement</h3>
      <p>The Professional Programs here assure a career start in the Hospitality &amp; International Cruise Line Industry.</p>
    </div>
    <div class="feature">
      <div class="feature-icon"><svg width="54" height="52" viewBox="0 0 54 52"><rect x="6" y="8" width="42" height="28" fill="none" stroke="#2a7d7c" stroke-width="3"/><rect x="12" y="14" width="30" height="16" fill="#2a7d7c"/><path d="M20 44h14M27 36v8" stroke="#2a7d7c" stroke-width="3"/></svg></div>
      <h3>Cutting Edge Training</h3>
      <p>The Professional Programs here assure a career start in the Hospitality &amp; International Cruise Line Industry.</p>
    </div>
    <div class="feature">
      <div class="feature-icon"><svg width="52" height="52" viewBox="0 0 52 52" fill="#2a7d7c"><path d="M26 6l20 10H6z"/><rect x="10" y="20" width="5" height="18"/><rect x="20" y="20" width="5" height="18"/><rect x="30" y="20" width="5" height="18"/><rect x="38" y="20" width="5" height="18"/><rect x="6" y="40" width="40" height="5"/></svg></div>
      <h3>Award Winning</h3>
      <p>The Professional Programs here assure a career start in the Hospitality &amp; International Cruise Line Industry.</p>
    </div>
  </div>
</section>

<section class="section programs">
  <h2 class="section-title">Find Hospitality and&nbsp; internships abroad now</h2>

  <article class="card" style="top:134px;left:135px">
    <div class="card-photo" role="img" aria-label="Chefs plating dishes in a kitchen" style="background:linear-gradient(135deg,#e9e6e2,#b9b2aa)"></div>
    <div class="card-meta"><span>▭ 97 REVIEWS</span><span class="stars">★★★★★</span><span>5.00</span><svg class="heart" width="16" height="14" viewBox="0 0 16 14"><path d="M8 14L1.5 7.5A3.8 3.8 0 018 2.3a3.8 3.8 0 016.5 5.2z" fill="#2aa7a3"/></svg></div>
    <h3>Hospitality, Sports, Tourism &amp;Hotel internship in China</h3>
    <p class="card-tags">// Culinary · F&amp;B · Front Office</p>
    <span class="btn">view more</span>
  </article>

  <article class="card" style="top:134px;left:628px">
    <div class="card-photo" role="img" aria-label="Smiling intern outdoors" style="background:linear-gradient(135deg,#7f8c5e,#4a5a3a)"></div>
    <div class="card-meta"><span>▭ 97 REVIEWS</span><span class="stars">★★★★★</span><span>5.00</span><svg class="heart" width="16" height="14" viewBox="0 0 16 14"><path d="M8 14L1.5 7.5A3.8 3.8 0 018 2.3a3.8 3.8 0 016.5 5.2z" fill="#2aa7a3"/></svg></div>
    <h3>Intern in China with Top 500 Companies in Engineering,</h3>
    <p class="card-tags">- Guest Relations</p>
    <span class="btn">view more</span>
  </article>

  <article class="card" style="top:576px;left:135px">
    <div class="card-photo" role="img" aria-label="Resort pool with palm trees at dusk" style="background:linear-gradient(180deg,#3b5a8c,#d8a070 60%,#2b4d6a)"></div>
    <div class="card-meta"><span>▭ 97 REVIEWS</span><span class="stars">★★★★★</span><span>5.00</span><svg class="heart" width="16" height="14" viewBox="0 0 16 14"><path d="M8 14L1.5 7.5A3.8 3.8 0 018 2.3a3.8 3.8 0 016.5 5.2z" fill="#2aa7a3"/></svg></div>
    <h3>Intern in China with Top 500 Companies in Engineering,</h3>
    <p class="card-tags">- Guest Relations</p>
    <span class="btn">view more</span>
  </article>

  <article class="card" style="top:576px;left:628px">
    <div class="card-photo" role="img" aria-label="Guests dining in a restaurant" style="background:linear-gradient(135deg,#7a4a3a,#c89a7a)"></div>
    <div class="card-meta"><span>▭ 97 REVIEWS</span><span class="stars">★★★★★</span><span>5.00</span><svg class="heart" width="16" height="14" viewBox="0 0 16 14"><path d="M8 14L1.5 7.5A3.8 3.8 0 018 2.3a3.8 3.8 0 016.5 5.2z" fill="#2aa7a3"/></svg></div>
    <h3>Intern in China with Top 500 Companies in Engineering,</h3>
    <p class="card-tags">- Guest Relations</p>
    <span class="btn">view more</span>
  </article>
</section>

<section class="section destinations" role="img" aria-label="Dim city skyline backdrop">
  <h2 class="section-title">Top Professional Destinations</h2>
  <div class="dest-tile" style="left:135px;width:304px;background:linear-gradient(180deg,#c98a5a,#8a5a44)" role="img" aria-label="City skyline at sunset">CHINA</div>
  <div class="dest-tile" style="left:465px;width:301px;background:linear-gradient(180deg,#9aa4a4,#4f6a5e)" role="img" aria-label="Aerial view of a river city">SPAIN</div>
  <div class="dest-tile" style="left:792px;width:301px;background:linear-gradient(180deg,#b9a58c,#7a6450)" role="img" aria-label="Historic palace facade">FRANCE</div>
  <span class="btn">More Professional Destinations</span>
</section>

<section class="section articles">
  <h2 class="section-title">Latest Articles</h2>
  <article class="article" style="left:98px">
    <div class="article-photo" role="img" aria-label="Chefs in white uniforms holding plates" style="background:linear-gradient(135deg,#e2ddd6,#8f8578)"></div>
    <h3>ACCREDITATIONS</h3><time>September 14, 2018</time><p>Sizzling Cook-off at the Appetite Festival</p>
  </article>
  <article class="article" style="left:443px">
    <div class="article-photo" role="img" aria-label="White resort buildings beside a pool" style="background:linear-gradient(180deg,#5a7fa8,#e8e2d8 55%,#7a8a7a)"></div>
    <h3>PARTNERSHIPS</h3><time>September 14, 2018</time><p>Sizzling Cook-off at the Appetite Festival</p>
  </article>
  <article class="article" style="left:789px">
    <div class="article-photo" role="img" aria-label="Crowd at an evening award event" style="background:linear-gradient(135deg,#2d4a7a,#6a88b0)"></div>
    <h3>AWARDS</h3><time>September 14, 2018</time><p>Sizzling Cook-off at the Appetite Festival</p>
  </article>
</section>

<section class="section contact">
  <h2>Hospitality internships are our specialty! Take your paid internship in<br>one of our top international five-star hotels</h2>
  <div class="field" style="top:206px;left:248px;width:326px">Name</div>
  <div class="field" style="top:206px;left:604px;width:326px">Last Name</div>
  <div class="field" style="top:256px;left:248px;width:326px">Email</div>
  <div class="field" style="top:256px;left:604px;width:326px">Asunto</div>
  <div class="field" style="top:306px;left:248px;width:682px">Subject</div>
  <div class="send">SEND</div>
</section>

<footer class="section footer">
  <div class="footer-col" style="left:170px"><h4>Link</h4><ul><li>Company</li><li>About Us</li><li>Careers</li><li>Press</li><li>Company Blog</li><li>Contact Us</li></ul></div>
  <div class="footer-col" style="left:316px"><h4>Providers</h4><ul><li>Login</li><li>Start Here</li><li>Advertise</li><li>Hire Teachers</li></ul></div>
  <div class="footer-col" style="left:464px"><h4>Community</h4><ul><li>Login</li><li>How It Works</li><li>Review Guidelines</li><li>Scholarships</li></ul></div>
  <div class="footer-col" style="left:632px"><h4>Join us on</h4><div class="socials"><span></span><span></span><span></span><span></span></div></div>
  <div class="footer-col" style="left:818px"><h4>Subscribe to the newsletter</h4><div class="newsletter-input">Your Email Address</div><div class="newsletter-btn">Send</div></div>
  <div class="footer-rule"></div>
  <p class="copyright">© 2023 by WAYFARER ACADEMY. Proudly created with SiteLoom.example</p>
</footer>

</body>
</html>
```